Window Cleaning Flyer targeting Shopfronts and Small Commercial Work

Single page flyer similar to the flyer targeting small commercial work and shopfronts

Please include the following text:

Brisk Pane Services delivers high quality service to suburbs all around Melbourne. From Frankston to Kalkallo, Brisk has you covered!

With over 10 years experience, Brisk specialises in providing:
- Window Cleaning: via elevated work platforms, rope access and extension poles
- Pressure Cleaning: Including chlorine treatment to prevent mould regrowth on concrete area
- Roof Gutter Cleaning: using our ladder free gutter vacuum

We pride ourselves on neat and professional presentation and vast geographical reach across Melbourne.

Our services can be completed on a frequency that meets your window cleaning needs. Whether a weekly clean or a yearly service.

Brisk Pane Services Melbourne takes care of all your window cleaning needs.

Contact Us now for free quote!

Target Market(s)

Small business and commercial building owners

Industry/Entity Type

Window Cleaning

Requirements
Must have
• Only use photos/logos provided
Should not have
• Stock phots

```html
<!DOCTYPE html>
<html lang="en">
<head>
<meta charset="utf-8">
<title>Brisk Pane Services – Free Quote Flyer</title>
<link href="https://fonts.googleapis.com/css2?family=Roboto:wght@400;500;700&display=swap" rel="stylesheet">
<style>
  :root {
    --ink: #000000;
    --paper: #ffffff;
    --accent: #fff200;
    --brand-blue: #0d4f8b;
    --rule: #e6e6e6;
    --muted: #dcdcdc;
  }
  * { box-sizing: border-box; margin: 0; padding: 0; }
  html, body { width: 948px; height: 1200px; overflow: hidden; background: var(--ink); }
  body { font-family: "Roboto", Arial, sans-serif; color: var(--paper); }

  .flyer { position: relative; width: 948px; height: 1200px; background: var(--ink); overflow: hidden; }

  .service-tabs {
    position: absolute; top: 0; left: 0; width: 948px; height: 112px;
    display: grid; grid-template-columns: 318px 316px 314px;
  }
  .service-tab {
    display: flex; align-items: center; justify-content: center;
    color: var(--accent); font-weight: 700; font-size: 22px; letter-spacing: 0.2px;
    border-right: 2px solid var(--rule); white-space: nowrap;
  }
  .service-tab:last-child { border-right: none; }

  .photo-strip {
    position: absolute; top: 112px; left: 0; width: 948px; height: 680px;
    display: grid; grid-template-columns: 318px 316px 314px;
  }
  .photo { border-right: 2px solid var(--rule); }
  .photo:last-child { border-right: none; }
  .photo--window { background: linear-gradient(160deg, #8d8d8d 0%, #555 55%, #3a3a3a 100%); }
  .photo--gutter { background: linear-gradient(180deg, #6e6e6e 0%, #3d3d3d 60%, #262626 100%); }
  .photo--pressure { background: linear-gradient(180deg, #a0a0a0 0%, #5a5a5a 45%, #333 100%); }

  .grid-line { position: absolute; left: 0; width: 948px; height: 2px; background: var(--rule); opacity: 0.85; }
  .grid-line--upper { top: 235px; }
  .grid-line--lower { top: 665px; }

  .headline {
    position: absolute; top: 360px; left: 0; width: 948px; text-align: center;
    color: var(--accent); font-weight: 500; font-size: 112px; line-height: 1; letter-spacing: 1px;
    white-space: nowrap;
  }
  .tagline {
    position: absolute; top: 480px; left: 0; width: 948px; text-align: center;
    font-weight: 500; font-size: 37px; color: var(--paper);
    text-shadow: 0 2px 6px rgba(0,0,0,0.6); white-space: nowrap;
  }

  .accent-bar { position: absolute; top: 792px; left: 0; width: 948px; height: 14px; background: var(--accent); }

  .brand-box {
    position: absolute; top: 740px; left: 354px; width: 240px; height: 150px;
    background: var(--brand-blue);
    display: flex; flex-direction: column; align-items: center; justify-content: center; gap: 6px;
    color: var(--accent); font-weight: 700; text-align: center;
  }
  .brand-box .brand-name { font-size: 40px; line-height: 1; letter-spacing: 1px; }
  .brand-box .brand-sub { font-size: 15px; letter-spacing: 1.5px; }

  .info { position: absolute; top: 820px; left: 0; width: 948px; height: 380px; }
  .col { position: absolute; }
  .col--services { left: 28px; top: 12px; width: 290px; }
  .col--quality { left: 326px; top: 110px; width: 300px; }
  .col--experience { left: 640px; top: 12px; width: 290px; }

  .section-title { font-size: 22px; font-weight: 500; margin-bottom: 10px; }
  .item { margin-bottom: 14px; }
  .item-title { color: var(--accent); font-weight: 700; font-size: 19px; line-height: 1.15; }
  .item-text { font-size: 13px; line-height: 1.3; color: var(--paper); }
  .item-text--bold { font-weight: 700; }

  .contact {
    position: absolute; left: 634px; top: 250px; width: 296px; height: 118px;
    border: 2px solid var(--muted); padding: 14px 20px;
    display: flex; flex-direction: column; justify-content: center; gap: 2px;
  }
  .contact-title { font-size: 21px; font-weight: 500; line-height: 1.2; white-space: nowrap; }
  .contact-phone { color: var(--accent); font-size: 30px; font-weight: 700; line-height: 1.2; white-space: nowrap; }
  .contact-web { font-size: 14px; font-weight: 500; line-height: 1.3; white-space: nowrap; }
</style>
</head>
<body>
<main class="flyer">
  <header class="service-tabs">
    <div class="service-tab">WINDOW CLEANING</div>
    <div class="service-tab">ROOF GUTTER CLEANING</div>
    <div class="service-tab">PRESSURE CLEANING</div>
  </header>

  <section class="photo-strip">
    <div class="photo photo--window" role="img" aria-label="Black and white photo of a worker cleaning a building's louvred windows with an extension pole"></div>
    <div class="photo photo--gutter" role="img" aria-label="Black and white photo of gutter cleaning on a brick building from an elevated platform"></div>
    <div class="photo photo--pressure" role="img" aria-label="Black and white photo of a worker pressure cleaning a house verandah"></div>
  </section>
  <div class="grid-line grid-line--upper"></div>
  <div class="grid-line grid-line--lower"></div>

  <h1 class="headline">FREE QUOTE!</h1>
  <p class="tagline">Takes care of all your Window Cleaning needs!</p>

  <div class="accent-bar"></div>
  <div class="brand-box">
    <span class="brand-name">BRISK</span>
    <span class="brand-sub">PANE SERVICES</span>
  </div>

  <section class="info">
    <div class="col col--services">
      <h2 class="section-title">OUR SERVICES</h2>
      <div class="item">
        <h3 class="item-title">Window Cleaning</h3>
        <p class="item-text">Via elevated work platforms, rope access and extension poles.</p>
      </div>
      <div class="item">
        <h3 class="item-title">Roof Gutter Cleaning</h3>
        <p class="item-text">Cleaning using our ladder free gutter vacuum.</p>
      </div>
      <div class="item">
        <h3 class="item-title">Pressure Cleaning</h3>
        <p class="item-text item-text--bold">Including chlorine treatment to prevent mould regrowth on concrete area.</p>
      </div>
    </div>

    <div class="col col--quality">
      <div class="item">
        <h3 class="item-title">Delivers High Quality Service</h3>
        <p class="item-text">To suburbs all around Melbourne. From Frankston to Kalkallo. Brisk has you covered!</p>
      </div>
      <div class="item">
        <h3 class="item-title">Weekly or Yearly Service</h3>
        <p class="item-text">Our service can be completed on a frequency that meets your window cleaning needs.</p>
      </div>
    </div>

    <div class="col col--experience">
      <div class="item">
        <h3 class="item-title">10 years Experience</h3>
        <p class="item-text">We pride ourselves on neat and professional presentation and vast geographical reach across Melbourne.</p>
      </div>
    </div>

    <div class="contact">
      <div class="contact-title">CONTACT US</div>
      <div class="contact-phone">000-000-000-000</div>
      <div class="contact-web">www.briskpaneservices.com</div>
    </div>
  </section>
</main>
</body>
</html>
```